Stationary Design using supplied logo

24 Hour Completion required after acceptance

Business Cards
Letter Head
With Compliments Slips
Web Page Theme

Please only use a the following colors:

Red
Charcoal
Chrome/Silver
White

Red being the DOMINANT Color

Please email questions you may have.

Continued work available to suitably motivated designer.

```html
<!DOCTYPE html>
<html lang="en">
<head>
<meta charset="utf-8">
<title>Vale Crest Letterhead</title>
<link href="https://fonts.googleapis.com/css2?family=Montserrat:wght@400;500;800&family=Open+Sans:ital,wght@1,600&display=swap" rel="stylesheet">
<style>
  :root {
    --red: #c01f2f;
    --charcoal: #6d6e71;
    --silver: #8b8c8f;
    --paper: #f7f7f7;
    --frame: #cfcfcf;
    --ink: #222222;
    --white: #ffffff;
  }
  * { box-sizing: border-box; margin: 0; padding: 0; }
  html, body { width: 900px; height: 1200px; overflow: hidden; background: var(--frame); }
  .letterhead {
    position: relative; width: 900px; height: 1200px;
    background: var(--frame); font-family: "Montserrat", sans-serif;
  }
  .sheet {
    position: absolute; left: 8px; top: 8px; width: 884px; height: 1184px;
    background: var(--paper); overflow: hidden;
  }
  .header-art { position: absolute; left: 0; top: 0; }
  .emblem-name {
    position: absolute; left: 100px; top: 96px; width: 180px; text-align: center;
    font-weight: 500; font-size: 26px; line-height: 30px; color: var(--red);
  }
  .brand-block { position: absolute; left: 548px; top: 22px; width: 322px; }
  .brand-name {
    font-weight: 800; font-size: 34px; line-height: 34px; color: var(--red); letter-spacing: 0.5px;
  }
  .brand-tagline {
    margin-left: 60px; margin-top: -3px; font-size: 11px; line-height: 13px;
    color: var(--charcoal); font-weight: 500;
  }
  .brand-intro {
    margin-top: 3px; font-family: "Open Sans", sans-serif; font-style: italic; font-weight: 600;
    font-size: 10px; line-height: 12.5px; color: var(--ink);
  }
  .cash-photo {
    position: absolute; left: 300px; top: 640px; width: 520px; height: 420px;
    background: radial-gradient(ellipse at 55% 50%, rgba(215,215,210,0.55) 0%, rgba(230,230,226,0.35) 45%, rgba(247,247,247,0) 72%);
  }
  .corner-arcs { position: absolute; left: 0; top: 0; }
  .wallet-icon {
    position: absolute; left: 774px; top: 1098px; width: 92px; height: 64px; border-radius: 8px;
    background: linear-gradient(135deg, #2b2b2b 0%, #4a4a4a 55%, #c9a441 56%, #e6c766 100%);
  }
  .contact-band {
    position: absolute; left: 0; width: 602px; height: 40px; display: flex; align-items: center;
    padding-left: 12px; color: var(--white); font-size: 13px; letter-spacing: 0.3px;
  }
  .contact-address { top: 1066px; background: var(--red); }
  .contact-phone { top: 1106px; background: var(--charcoal); }
  .contact-email { top: 1146px; height: 38px; background: var(--silver); }
</style>
</head>
<body>
<div class="letterhead">
  <div class="sheet">
    <svg class="header-art" width="884" height="200" viewBox="0 0 884 200">
      <rect x="0" y="115" width="884" height="7" fill="var(--red)"/>
      <ellipse cx="190" cy="110" rx="112" ry="76" fill="var(--red)"/>
      <ellipse cx="190" cy="112" rx="102" ry="68" fill="var(--white)"/>
    </svg>
    <div class="emblem-name">Vale Crest</div>

    <div class="brand-block">
      <div class="brand-name">Vale Crest</div>
      <div class="brand-tagline">Savings Made Simple</div>
      <p class="brand-intro">Lorem Ipsum is simply dummy text of the printing and typesetting industry Lorem Ipsum is simply dummy text of the printing and type-setting industry.</p>
    </div>

    <div class="cash-photo" role="img" aria-label="Faint photo of a hand fanning out banknotes"></div>

    <svg class="corner-arcs" width="884" height="1184" viewBox="0 0 884 1184">
      <circle cx="900" cy="1245" r="348" fill="var(--silver)"/>
      <circle cx="900" cy="1245" r="290" fill="var(--charcoal)"/>
      <circle cx="900" cy="1245" r="212" fill="var(--red)"/>
    </svg>
    <div class="wallet-icon" role="img" aria-label="Illustration of a wallet with banknotes and a gold coin"></div>

    <div class="contact-band contact-address">NORTHWICK IT SOLUTIONS UNIT 4 2ND FLOOR SECTOR 9 ASHFORD</div>
    <div class="contact-band contact-phone">Mobile No : +91-800 555 0142, +91-9000555017</div>
    <div class="contact-band contact-email">Email : hello@northwickit.example</div>
  </div>
</div>
</body>
</html>
```